Building Company Business Card Design

I am looking to get a business card designed for my Building Company. Please find the logo attached.

Industry/Entity Type

Business

Contact Information for Business Card

Mobile 0472 913 046
Email admin@tarrowconstructworks.com.au
Website www.tarrowconstructworks.com.au

Colors
0255a3

```html
<!DOCTYPE html>
<html lang="en">
<head>
<meta charset="utf-8">
<title>Tarrow Construct Works – Business Card</title>
<link href="https://fonts.googleapis.com/css2?family=Montserrat:wght@700&family=Lato:wght@700&display=swap" rel="stylesheet">
<style>
  :root {
    --brand-blue: #0255a3;
    --brand-grey: #5f6166;
    --card-white: #f7f8fc;
    --sky-light: #c3c8e6;
    --sky-mid: #8f9bd0;
    --sky-deep: #5a70bb;
    --page-bg: #dfe9f2;
    --rule-grey: #8a8c91;
  }
  * { margin: 0; padding: 0; box-sizing: border-box; }
  html, body { width: 1200px; height: 1042px; overflow: hidden; }
  body {
    background: var(--page-bg);
    display: flex;
    flex-direction: column;
    align-items: center;
    justify-content: center;
    gap: 60px;
    font-family: "Lato", sans-serif;
  }
  .card {
    position: relative;
    width: 700px;
    height: 400px;
    background: var(--card-white);
    overflow: hidden;
    box-shadow: 0 10px 30px rgba(20, 60, 110, 0.18);
  }
  .brand-name {
    font-family: "Montserrat", sans-serif;
    font-weight: 700;
    color: var(--brand-blue);
    text-transform: uppercase;
    letter-spacing: 0.04em;
    line-height: 1.05;
    text-align: center;
  }

  /* Front */
  .card-front .brand-name {
    position: absolute;
    top: 58px;
    left: 0;
    right: 0;
    font-size: 44px;
  }
  .skyline {
    position: absolute;
    left: 0;
    right: 0;
    bottom: 0;
    height: 210px;
    background: linear-gradient(180deg, var(--sky-light) 0%, var(--sky-mid) 55%, var(--sky-deep) 100%);
    opacity: 0.85;
  }
  .web-band {
    position: absolute;
    left: 0;
    right: 0;
    top: 245px;
    height: 62px;
    background: var(--brand-blue);
    display: flex;
    align-items: center;
    justify-content: center;
  }
  .web-band .website {
    color: #ffffff;
    font-size: 20px;
    letter-spacing: 0.16em;
  }

  /* Back */
  .card-back .brand-watermark {
    position: absolute;
    top: 40px;
    left: 0;
    right: 0;
    font-size: 72px;
    color: var(--brand-blue);
    opacity: 0.07;
  }
  .card-back .brand-name.main {
    position: absolute;
    top: 92px;
    left: 0;
    right: 0;
    font-size: 30px;
  }
  .divider {
    position: absolute;
    top: 190px;
    left: 200px;
    width: 300px;
    height: 2px;
    background: linear-gradient(90deg, transparent, var(--rule-grey) 20%, var(--rule-grey) 80%, transparent);
  }
  .contact-list {
    position: absolute;
    top: 220px;
    left: 0;
    right: 0;
    list-style: none;
    display: flex;
    flex-direction: column;
    align-items: center;
    gap: 16px;
  }
  .contact-item {
    display: flex;
    align-items: center;
    gap: 10px;
    color: var(--brand-blue);
    font-size: 22px;
    letter-spacing: 0.05em;
  }
  .contact-item svg { width: 22px; height: 22px; flex: none; }
</style>
</head>
<body>

<section class="card card-front" aria-label="Business card front">
  <div class="skyline" role="img" aria-label="Soft blue city skyline silhouette"></div>
  <div class="web-band">
    <span class="website">www.tarrowconstructworks.com.au</span>
  </div>
  <p class="brand-name">Tarrow Construct Works</p>
</section>

<section class="card card-back" aria-label="Business card back">
  <p class="brand-name brand-watermark" aria-hidden="true">Tarrow</p>
  <p class="brand-name main">Tarrow Construct Works</p>
  <div class="divider"></div>
  <ul class="contact-list">
    <li class="contact-item">
      <svg viewBox="0 0 24 24" aria-hidden="true">
        <rect x="2" y="5" width="20" height="14" fill="var(--brand-grey)"/>
        <path d="M2 5 L12 13 L22 5" fill="none" stroke="#ffffff" stroke-width="1.6"/>
      </svg>
      <span>admin@tarrowconstructworks.com.au</span>
    </li>
    <li class="contact-item">
      <svg viewBox="0 0 24 24" aria-hidden="true">
        <circle cx="12" cy="12" r="11" fill="var(--brand-grey)"/>
        <path d="M9 6.5c-1.5 0.6-2 2-1.4 3.8 0.9 2.6 2.8 4.8 5.3 6 1.7 0.8 3.1 0.4 3.8-1l-2-1.8-1.5 0.9c-1.3-0.7-2.4-1.9-3-3.2l1-1.4z" fill="#ffffff"/>
      </svg>
      <span>0472 913 046</span>
    </li>
  </ul>
</section>

</body>
</html>
```